Visitenkarten-Design für Süßigkeiten-Onlineshop
Zielgruppe
Ich werde einen Onlineshop betreiben und Süßigkeiten aus aller Welt verkaufen.
Aufgabenstellung
Mein Logo sollte drauf sein. Die Visitenkarte kann auch bisschen stylischer gestaltet werden. Aber da lasse ich mich auch gerne überraschen.
Man könnte vielleicht noch den Slogan- Süßigkeiten aus aller Welt-
Mein Name sollte drauf stehen,
Jonas Brettel
Lindauer Weg 14
41562 Dormagen
E-Mail info@zuckerfuchs-shop.de
Instagram @zuckerfuchs.de
Facebook Zuckerfuchs
Tic Toc @zuckerfuhcs.de

```html
<!DOCTYPE html>
<html lang="de">
<head>
<meta charset="utf-8">
<title>Zuckerfuchs – Visitenkarte</title>
<link href="https://fonts.googleapis.com/css2?family=Oswald:wght@200;300;400;500&family=Mrs+Saint+Delafield&display=swap" rel="stylesheet">
<style>
  :root {
    --page: #ececec;
    --card-white: #ffffff;
    --teal: #7fc4c9;
    --teal-dark: #1d8d99;
    --ink: #3a3a3a;
    --ink-script: #2e3b3d;
    --white: #ffffff;
  }
  * { box-sizing: border-box; margin: 0; padding: 0; }
  html, body {
    width: 1200px; height: 800px; overflow: hidden;
    background: var(--page);
  }
  .sheet {
    width: 1200px; height: 800px;
    display: flex; align-items: center; justify-content: center;
    gap: 40px;
  }
  .card {
    width: 540px; height: 348px;
    box-shadow: 0 2px 8px rgba(0,0,0,0.12);
    display: flex; flex-direction: column; align-items: center; justify-content: center;
    text-align: center;
  }
  /* Front */
  .card--front { background: var(--card-white); }
  .brand-mark {
    width: 150px; height: 150px; border-radius: 50%;
    background: var(--teal);
    margin-bottom: 26px;
  }
  .brand-name {
    font-family: "Oswald", sans-serif;
    font-weight: 400;
    font-size: 38px;
    letter-spacing: 5px;
    color: var(--ink);
  }
  /* Back */
  .card--back { background: var(--teal); color: var(--white); }
  .back-title {
    font-family: "Oswald", sans-serif;
    font-weight: 200;
    font-size: 66px;
    line-height: 1;
    letter-spacing: 1px;
    text-transform: uppercase;
  }
  .back-slogan {
    font-family: "Mrs Saint Delafield", cursive;
    font-size: 40px;
    color: var(--ink-script);
    line-height: 1.1;
    margin-top: 6px;
  }
  .back-owner {
    font-family: "Oswald", sans-serif;
    font-weight: 400;
    font-size: 22px;
    color: var(--teal-dark);
    margin-top: 14px;
  }
  .back-contact {
    font-family: "Oswald", sans-serif;
    font-weight: 400;
    font-size: 19px;
    margin-top: 4px;
  }
  .back-social {
    font-family: "Oswald", sans-serif;
    font-weight: 400;
    font-size: 13px;
    color: var(--teal-dark);
    letter-spacing: 1px;
    margin-top: 18px;
  }
  .back-handle {
    font-family: "Oswald", sans-serif;
    font-weight: 400;
    font-size: 17px;
    margin-top: 4px;
  }
</style>
</head>
<body>
  <main class="sheet">
    <section class="card card--front" aria-label="Vorderseite">
      <div class="brand-mark" aria-hidden="true"></div>
      <p class="brand-name">ZUCKERFUCHS</p>
    </section>

    <section class="card card--back" aria-label="Rückseite">
      <h1 class="back-title">Zuckerfuchs</h1>
      <p class="back-slogan">24/7 lecker Shoppen auf www.zuckerfuchs.de</p>
      <p class="back-owner">by Jonas Brettel</p>
      <p class="back-contact">01525.7304968 · Lindauer Weg 14 · 41562 Dormagen</p>
      <p class="back-social">INSTAGRAM · FACEBOOK · TIKTOK</p>
      <p class="back-handle">zuckerfuchs/zuckerfuchs.de</p>
    </section>
  </main>
</body>
</html>
```